Badass Woman-Owned and Operated Small Law Firm needs Modern & Interesting Powerpoint template...

Mainly need powerpoint template that works with high-quality photos and "clipart", but would also like template for post-card size marketing (invitations or announcements); a banner ad for other websites, a Pro Mesh Banner, and One-Page Newsletter/Flyer template to use as a marketing handout announcing new services, etc. I have a logo and colors and can show some designs we've done on our own to show you what we like.

Target Market(s)

managers of condos and hoas and members of condos and hoas

Industry/Entity Type

Law firm that represents condominiums and HOAs

Requirements
Must have
• use of theme/colors and logo already established
Nice to have
• For the powerpoint, I like faded images in the background along with interesting layout. So tired of just banners at the top and bottom

```html
<!DOCTYPE html>
<html lang="en">
<head>
<meta charset="utf-8">
<title>Harborline Residential Law – Brand Collateral Board</title>
<link rel="stylesheet" href="https://fonts.googleapis.com/css2?family=Montserrat:wght@300;400;500&family=Poppins:ital,wght@0,300;0,700;0,800;1,600;1,700&family=Barlow+Semi+Condensed:wght@600&display=swap">
<style>
:root{
  --olive:#9a9b3e;
  --olive-soft:#b4b55a;
  --ink:#232323;
  --ink-deep:#1a1a1a;
  --paper:#ffffff;
  --board:#c4c4c4;
  --board-dark:#8f8f8f;
  --label-grey:#7a7a7a;
}
*{margin:0;padding:0;box-sizing:border-box}
html,body{width:868px;height:1200px;overflow:hidden}
body{
  position:relative;
  font-family:"Montserrat",sans-serif;
  background:linear-gradient(160deg,var(--board-dark) 0%,#a9a9a9 22%,var(--board) 45%,#d6d6d6 100%);
}
.section-label{
  position:absolute;font-family:"Montserrat",sans-serif;font-weight:300;
  letter-spacing:.12em;text-transform:uppercase;white-space:nowrap;transform:translateX(-50%);
}
.section-label--light{color:#fff}
.section-label--grey{color:var(--label-grey)}
.piece{position:absolute;overflow:hidden;box-shadow:10px 10px 0 rgba(255,255,255,.28)}
.piece > svg{position:absolute;inset:0}
.brand{position:absolute;display:flex;align-items:center;gap:5px}
.brand-dot{border-radius:50%;background:var(--olive);flex:none}
.brand-name{font-family:"Barlow Semi Condensed",sans-serif;font-weight:600;line-height:1.02;text-transform:uppercase}
.tagline{position:absolute;font-family:"Poppins",sans-serif;line-height:1.15}
.tagline .lead{font-weight:300;font-style:normal}
.tagline em{font-weight:700;font-style:italic}
.tagline strong{font-weight:800;color:var(--olive)}
.contact-row{position:absolute;display:flex;align-items:center;white-space:nowrap}
.contact-row span{display:inline-flex;align-items:center;gap:3px}
.icon{display:inline-block}
.fine-print{font-family:"Montserrat",sans-serif;line-height:1.35}
.heading-olive{font-family:"Poppins",sans-serif;font-weight:800;color:var(--olive);text-transform:uppercase}

.slide{left:202px;top:69px;width:436px;height:244px}
.invite-front{left:38px;top:386px;width:376px;height:250px}
.invite-title{position:absolute;left:0;right:0;text-align:center;color:#fff;font-family:"Poppins",sans-serif;font-weight:800;line-height:1}
.invite-back{left:431px;top:386px;width:375px;height:250px;background:var(--paper)}
.bullets{position:absolute;list-style:none;color:#fff;font-size:10px;display:grid;grid-template-columns:auto auto;column-gap:12px;row-gap:3px}
.bullets li::before{content:"";display:inline-block;width:4px;height:4px;border-radius:50%;background:var(--olive);margin-right:5px;vertical-align:middle}
.flyer{left:33px;top:711px;width:324px;height:457px;background:var(--ink)}
.flyer-col{position:absolute;top:371px;width:130px;color:#e6e6e6}
.flyer-col p{font-size:3.6px;margin-top:2px}
.web-banner{left:385px;top:711px;width:398px;height:199px;background:var(--ink)}
.cover{left:385px;top:1000px;width:457px;height:77px;background:var(--ink)}
</style>
</head>
<body>

<!-- ===== Presentation template ===== -->
<div class="section-label section-label--light" style="left:434px;top:27px;font-size:21px">Presentation Template</div>
<section class="piece slide" aria-label="Presentation title slide">
  <svg width="436" height="244" viewBox="0 0 436 244">
    <defs>
      <clipPath id="slideClip"><path d="M110,7 H417 Q429,7 429,19 V120 C420,190 380,230 320,237 H19 Q7,237 7,225 V130 C10,80 50,30 110,7 Z"/></clipPath>
      <linearGradient id="slidePhoto" x1="0" y1="0" x2="0" y2="1">
        <stop offset="0" stop-color="#2c2f2a"/><stop offset=".5" stop-color="#3a3a32"/><stop offset="1" stop-color="#1e1e1c"/>
      </linearGradient>
    </defs>
    <rect width="436" height="244" fill="var(--olive)"/>
    <path d="M7,7 H110 C50,30 10,80 7,130 Z" fill="#fff"/>
    <path d="M429,120 C420,190 380,230 320,237 H429 Z" fill="#fff"/>
    <path d="M110,7 H417 Q429,7 429,19 V120 C420,190 380,230 320,237 H19 Q7,237 7,225 V130 C10,80 50,30 110,7 Z" fill="var(--ink)"/>
    <g clip-path="url(#slideClip)">
      <rect x="7" y="60" width="422" height="177" fill="url(#slidePhoto)" opacity=".75" role="img" aria-label="Faded evening photo of a craftsman-style house among trees"/>
      <rect x="7" y="150" width="422" height="90" fill="var(--ink)" opacity=".55"/>
    </g>
    <line x1="38" y1="160" x2="398" y2="160" stroke="#fff" stroke-width="1.2" stroke-dasharray="1.5 2"/>
  </svg>
  <div class="brand" style="left:135px;top:48px">
    <span class="brand-dot" style="width:30px;height:30px"></span>
    <span class="brand-name" style="color:#fff;font-size:15px">Harborline<br>Residential Law</span>
  </div>
  <p class="tagline" style="left:0;right:0;top:123px;text-align:center;font-size:12.5px;color:#fff">
    <span class="lead">SERVING</span> <em>WASHINGTON AND OREGON COMMUNITY</em><br>
    <strong>ASSOCIATIONS OF ALL AGES, SHAPES, AND SIZES</strong>
  </p>
  <div class="contact-row" style="left:86px;top:213px;gap:10px;color:#fff;font-size:8.5px">
    <span><svg class="icon" width="8" height="8" viewBox="0 0 10 10"><path d="M2,1 L4,1 L5,3 L3.8,4 Q5,6.2 6,6.2 L7,5 L9,6 L9,8 Q8,9.5 6,9 Q1,7 1,2 Z" fill="var(--olive)"/></svg>555-014-2290</span>
    <span><svg class="icon" width="9" height="7" viewBox="0 0 12 8"><rect x=".5" y=".5" width="11" height="7" fill="none" stroke="var(--olive)"/><path d="M.5,.5 L6,5 L11.5,.5" fill="none" stroke="var(--olive)"/></svg>info@hblaw.example</span>
    <span><svg class="icon" width="8" height="8" viewBox="0 0 10 10"><circle cx="5" cy="5" r="4.3" fill="none" stroke="var(--olive)"/><ellipse cx="5" cy="5" rx="2" ry="4.3" fill="none" stroke="var(--olive)"/><line x1=".7" y1="5" x2="9.3" y2="5" stroke="var(--olive)"/></svg>www.hblaw.example</span>
  </div>
</section>

<!-- ===== Invitation ===== -->
<div class="section-label section-label--light" style="left:423px;top:333px;font-size:29px">Invitation</div>

<section class="piece invite-front" aria-label="Invitation postcard front">
  <svg width="376" height="250" viewBox="0 0 376 250">
    <defs>
      <linearGradient id="teamPhoto" x1="0" y1="0" x2="1" y2="1"><stop offset="0" stop-color="#5a4a42"/><stop offset=".5" stop-color="#3b2f2c"/><stop offset="1" stop-color="#c9c5c0"/></linearGradient>
      <linearGradient id="duskHouse" x1="0" y1="0" x2="0" y2="1"><stop offset="0" stop-color="#c9a9b8"/><stop offset=".45" stop-color="#8a8f9e"/><stop offset=".8" stop-color="#6c7066"/><stop offset="1" stop-color="#4d5a3a"/></linearGradient>
    </defs>
    <rect width="376" height="250" fill="var(--ink)"/>
    <rect x="0" y="0" width="130" height="140" fill="url(#teamPhoto)" role="img" aria-label="Photo of three women reviewing documents at a table"/>
    <rect x="230" y="0" width="146" height="140" fill="url(#duskHouse)" role="img" aria-label="Photo of a two-storey suburban house at dusk"/>
    <ellipse cx="180" cy="30" rx="78" ry="112" fill="#fff"/>
    <path d="M0,143 Q188,97 376,138 V250 H0 Z" fill="var(--olive)"/>
    <path d="M0,156 Q188,110 376,150 V250 H0 Z" fill="var(--ink)"/>
  </svg>
  <div class="brand" style="left:118px;top:40px">
    <span class="brand-dot" style="width:28px;height:28px"></span>
    <span class="brand-name" style="color:var(--ink);font-size:13px">Harborline<br>Residential Law</span>
  </div>
  <div class="invite-title" style="top:134px;font-size:29px">YOU ARE</div>
  <div class="invite-title" style="top:160px;font-size:57px;letter-spacing:-.01em">INVITED</div>
  <p style="position:absolute;left:0;right:0;top:219px;text-align:center;font-size:11px;line-height:1.15;color:#fff">
    We are Serving Washington and Oregon<br><span style="color:var(--olive)">community associations of all ages, shapes, and sizes</span>
  </p>
</section>

<section class="piece invite-back" aria-label="Invitation postcard back">
  <svg width="375" height="250" viewBox="0 0 375 250">
    <path d="M0,0 H170 C205,60 205,190 182,250 H0 Z" fill="var(--olive)"/>
    <path d="M0,0 H158 C192,60 192,185 168,250 H0 Z" fill="var(--ink)"/>
    <path d="M0,198 H186 C185,222 184,238 182,250 H0 Z" fill="var(--olive)"/>
    <rect x="308.5" y="19.5" width="46" height="46" fill="none" stroke="var(--ink)" stroke-width="1"/>
    <g stroke="var(--ink)" stroke-width=".8">
      <line x1="217" y1="85" x2="354" y2="85"/><line x1="217" y1="101" x2="354" y2="101"/>
      <line x1="217" y1="116" x2="354" y2="116"/><line x1="217" y1="132" x2="354" y2="132"/>
      <line x1="217" y1="148" x2="354" y2="148"/><line x1="217" y1="165" x2="354" y2="165"/>
    </g>
  </svg>
  <div class="brand" style="left:13px;top:20px">
    <span class="brand-dot" style="width:30px;height:30px"></span>
    <span class="brand-name" style="color:#fff;font-size:13px">Harborline<br>Residential Law</span>
  </div>
  <div class="heading-olive" style="position:absolute;left:12px;top:69px;font-size:12.5px">Our Services:</div>
  <div class="fine-print" style="position:absolute;left:12px;top:89px;width:145px;color:#fff;font-size:3.7px">
    <p>At our firm we act as one part of the management team for each client. Associations are more than groups of owners; they hold real assets, so we help boards and managers understand their duties, the limits of their authority and the steps set out in their governing documents.</p>
    <p style="margin-top:4px">Please see our Services page for more detail on the work we provide.</p>
  </div>
  <div class="heading-olive" style="position:absolute;left:12px;top:146px;font-size:12.5px">How We Work:</div>
  <ul class="bullets" style="left:12px;top:166px">
    <li>Responsive</li><li>Ready</li><li>Efficient</li>
  </ul>
  <div style="position:absolute;left:12px;top:205px;color:#fff">
    <div style="display:flex;align-items:center;gap:4px;font-family:'Poppins',sans-serif;font-weight:800;font-size:14px;line-height:1"><svg class="icon" width="11" height="11" viewBox="0 0 10 10"><path d="M2,1 L4,1 L5,3 L3.8,4 Q5,6.2 6,6.2 L7,5 L9,6 L9,8 Q8,9.5 6,9 Q1,7 1,2 Z" fill="var(--ink)"/></svg>555-014-2290</div>
    <div style="display:flex;align-items:center;gap:5px;font-size:9.5px;margin-top:3px"><svg class="icon" width="10" height="7" viewBox="0 0 12 8"><rect x=".5" y=".5" width="11" height="7" fill="none" stroke="var(--ink)"/><path d="M.5,.5 L6,5 L11.5,.5" fill="none" stroke="var(--ink)"/></svg>info@hblaw.example</div>
    <div style="display:flex;align-items:center;gap:5px;font-size:9.5px;margin-top:1px"><svg class="icon" width="10" height="10" viewBox="0 0 10 10"><circle cx="5" cy="5" r="4.3" fill="none" stroke="var(--ink)"/><ellipse cx="5" cy="5" rx="2" ry="4.3" fill="none" stroke="var(--ink)"/><line x1=".7" y1="5" x2="9.3" y2="5" stroke="var(--ink)"/></svg>www.hblaw.example</div>
  </div>
</section>

<!-- ===== Flyer ===== -->
<div class="section-label section-label--light" style="left:196px;top:658px;font-size:29px">Flyer</div>
<section class="piece flyer" aria-label="One-page flyer">
  <svg width="324" height="457" viewBox="0 0 324 457">
    <defs>
      <linearGradient id="flyerHouse" x1="0" y1="0" x2="0" y2="1"><stop offset="0" stop-color="#e4dde6"/><stop offset=".3" stop-color="#9aa0b2"/><stop offset=".6" stop-color="#6f7470"/><stop offset=".85" stop-color="#4a5a3a"/><stop offset="1" stop-color="#2b2b28"/></linearGradient>
      <linearGradient id="flyerFade" x1="0" y1="0" x2="0" y2="1"><stop offset="0" stop-color="var(--ink)" stop-opacity="0"/><stop offset="1" stop-color="var(--ink)"/></linearGradient>
      <linearGradient id="flyerTeam" x1="0" y1="0" x2="1" y2="1"><stop offset="0" stop-color="#6b5048"/><stop offset=".5" stop-color="#3a2d2a"/><stop offset="1" stop-color="#d8d4cf"/></linearGradient>
      <linearGradient id="flyerDesk" x1="0" y1="0" x2="1" y2="1"><stop offset="0" stop-color="#4b4a47"/><stop offset=".6" stop-color="#d9d6d0"/><stop offset="1" stop-color="#8d7a63"/></linearGradient>
    </defs>
    <rect width="324" height="280" fill="url(#flyerHouse)" role="img" aria-label="Photo of a grey two-storey family home at sunset"/>
    <rect y="200" width="324" height="110" fill="url(#flyerFade)"/>
    <circle cx="94" cy="183" r="74" fill="var(--olive)"/>
    <circle cx="94" cy="183" r="67" fill="url(#flyerTeam)" role="img" aria-label="Photo of three women reviewing paperwork together"/>
    <circle cx="231" cy="214" r="53" fill="var(--olive)"/>
    <circle cx="231" cy="214" r="47" fill="url(#flyerDesk)" role="img" aria-label="Photo of hands signing documents at a desk"/>
    <rect y="437" width="324" height="20" fill="var(--olive)"/>
  </svg>
  <div class="brand" style="left:228px;top:10px">
    <span class="brand-dot" style="width:20px;height:20px"></span>
    <span class="brand-name" style="color:var(--ink);font-size:8.5px">Harborline<br>Residential Law</span>
  </div>
  <p class="tagline" style="left:22px;top:277px;font-size:18.5px;line-height:1.13;color:#fff">
    <span class="lead">SERVING</span> <em>WASHINGTON<br>AND OREGON COMMUNITY</em><br>
    <strong>ASSOCIATIONS OF ALL AGES,<br>SHAPES, AND SIZES.</strong>
  </p>
  <div class="flyer-col fine-print" style="left:23px">
    <div class="heading-olive" style="font-size:7.5px">About Us:</div>
    <p>New name, same steady service. In 2023 we formed a cooperative firm focused on general counsel advice for condominium and HOA communities. If you valued the focused, responsive counsel we gave before, you have come to the right place.</p>
    <p style="margin-top:4px">Our founding partner, Dana Reyes, has served community associations and nonprofits since 2002, first in construction defect cases and later leading a general counsel group.</p>
  </div>
  <div class="flyer-col fine-print" style="left:175px">
    <div class="heading-olive" style="font-size:7.5px">Our Philosophy:</div>
    <p>Our philosophy is simple, yet easy for lawyers to forget: we are here to help!</p>
    <p style="margin-top:4px">We help best by taking the time to understand each client's situation, applying the law and governing documents in that context, weighing the risks of each option, and giving clear, practical advice to resolve the issue.</p>
    <p style="margin-top:4px">For more on how we carry out this mission, please see How We Work.</p>
  </div>
  <div class="contact-row" style="left:7px;top:440px;gap:9px;color:#fff;font-size:8.5px">
    <span style="font-family:'Poppins',sans-serif;font-weight:800;font-size:11px"><svg class="icon" width="9" height="9" viewBox="0 0 10 10"><path d="M2,1 L4,1 L5,3 L3.8,4 Q5,6.2 6,6.2 L7,5 L9,6 L9,8 Q8,9.5 6,9 Q1,7 1,2 Z" fill="var(--ink)"/></svg>555-014-2290</span>
    <span><svg class="icon" width="10" height="7" viewBox="0 0 12 8"><rect x=".5" y=".5" width="11" height="7" fill="none" stroke="var(--ink)"/><path d="M.5,.5 L6,5 L11.5,.5" fill="none" stroke="var(--ink)"/></svg>info@hblaw.example</span>
    <span><svg class="icon" width="9" height="9" viewBox="0 0 10 10"><circle cx="5" cy="5" r="4.3" fill="none" stroke="var(--ink)"/><ellipse cx="5" cy="5" rx="2" ry="4.3" fill="none" stroke="var(--ink)"/><line x1=".7" y1="5" x2="9.3" y2="5" stroke="var(--ink)"/></svg>www.hblaw.example</span>
  </div>
</section>

<!-- ===== Web banner ===== -->
<div class="section-label section-label--grey" style="left:579px;top:658px;font-size:29px">Web Banner</div>
<section class="piece web-banner" aria-label="Website banner ad">
  <svg width="398" height="199" viewBox="0 0 398 199">
    <defs>
      <linearGradient id="bannerTeam" x1="0" y1="0" x2="1" y2="1"><stop offset="0" stop-color="#6d5a4e"/><stop offset=".45" stop-color="#3a2c2a"/><stop offset="1" stop-color="#cfcac3"/></linearGradient>
      <linearGradient id="smallPhoto" x1="0" y1="0" x2="0" y2="1"><stop offset="0" stop-color="#7fa6d2"/><stop offset="1" stop-color="#d9dcd8"/></linearGradient>
    </defs>
    <rect x="223" y="0" width="175" height="199" fill="url(#bannerTeam)" role="img" aria-label="Photo of three women discussing documents"/>
    <path d="M0,88 H212 Q232,88 232,108 V152 Q232,172 212,172 H0 Z" fill="var(--olive)"/>
    <circle cx="229" cy="35" r="24" fill="var(--olive)"/><circle cx="229" cy="35" r="20" fill="#d7d5d0" role="img" aria-label="Photo of a signed contract"/>
    <circle cx="215" cy="106" r="26" fill="var(--olive)"/><circle cx="215" cy="106" r="22" fill="url(#smallPhoto)" role="img" aria-label="Photo of a white house"/>
    <circle cx="229" cy="164" r="24" fill="var(--olive)"/><circle cx="229" cy="164" r="20" fill="url(#smallPhoto)" role="img" aria-label="Photo of a townhouse row"/>
  </svg>
  <div style="position:absolute;left:16px;top:15px;color:#fff;font-family:'Poppins',sans-serif;font-weight:800;font-size:18.5px;line-height:1.08">HARBORLINE<br>RESIDENTIAL<br>LAW GROUP</div>
  <p class="tagline" style="left:15px;top:98px;font-size:12px;line-height:1.2;color:#fff">
    <span class="lead">SERVING</span> <em>WASHINGTON<br>AND OREGON COMMUNITY</em><br>
    <strong style="color:var(--ink)">ASSOCIATIONS OF ALL<br>AGES, SHAPES, AND SIZES</strong>
  </p>
</section>

<!-- ===== Pro Mesh cover ===== -->
<div class="section-label section-label--grey" style="left:577px;top:955px;font-size:29px">Pro Mesh Cover</div>
<section class="piece cover" aria-label="Pro Mesh profile cover">
  <svg width="457" height="77" viewBox="0 0 457 77">
    <defs>
      <linearGradient id="coverHomes" x1="0" y1="0" x2="1" y2="0"><stop offset="0" stop-color="#3b3d3a"/><stop offset=".4" stop-color="#7d8290"/><stop offset=".7" stop-color="#a9a7a5"/><stop offset="1" stop-color="#505550"/></linearGradient>
    </defs>
    <rect width="457" height="38" fill="url(#coverHomes)" opacity=".8" role="img" aria-label="Faded photo strip of suburban homes"/>
    <rect x="0" y="38" width="457" height="33" fill="var(--olive)"/>
    <rect x="0" y="71" width="457" height="6" fill="var(--ink-deep)"/>
  </svg>
  <div class="brand" style="left:362px;top:6px">
    <span class="brand-dot" style="width:22px;height:22px"></span>
    <span class="brand-name" style="color:#fff;font-size:8.5px">Harborline<br>Residential Law</span>
  </div>
  <p class="tagline" style="right:12px;top:41px;text-align:right;font-size:11.5px;line-height:1.18;color:#fff">
    <span class="lead">SERVING</span> <em>WASHINGTON AND OREGON COMMUNITY</em><br>
    <strong style="color:var(--ink)">ASSOCIATIONS OF ALL AGES, SHAPES, AND SIZES</strong>
  </p>
</section>

</body>
</html>
```